Business Card Design Project

Small privately owned salon.

Industry/Entity Type

Business

Contact Information for Business Card

Hair salon.i would like my logo to be my name , Marisol Denby. Address and phone can go on the front or back. The back will be where I write their appt.
address-362 Thistledown lane York, Pa. 17488
Phone- 717-555-0148

```html
<!DOCTYPE html>
<html lang="en">
<head>
<meta charset="utf-8">
<title>Marisol Denby Hair Salon – Business Card</title>
<link rel="stylesheet" href="https://fonts.googleapis.com/css2?family=Open+Sans:wght@400;600&display=swap">
<style>
  :root {
    --page-bg: #ece9e4;
    --card-dark: #0b0c0c;
    --card-light: #ffffff;
    --ink: #2b2b2b;
    --ink-soft: #555555;
    --on-dark: #ffffff;
    --rule: #3a3a3a;
  }
  * { margin: 0; padding: 0; box-sizing: border-box; }
  html, body {
    width: 1200px; height: 1000px; overflow: hidden;
    background: var(--page-bg);
    font-family: "Open Sans", Arial, sans-serif;
    color: var(--ink);
  }
  .canvas { position: relative; width: 1200px; height: 1000px; }

  .card {
    position: absolute;
    left: 289px;
    width: 622px;
    height: 365px;
    border-radius: 22px;
    overflow: hidden;
  }

  /* Front */
  .card-front { top: 124px; background: var(--card-dark); }
  .brand {
    position: absolute;
    right: 110px;
    top: 148px;
    text-align: right;
    color: var(--on-dark);
  }
  .brand-name {
    font-size: 46px;
    font-weight: 600;
    line-height: 1;
    letter-spacing: 0.5px;
  }
  .brand-tagline {
    margin-top: 26px;
    font-size: 22px;
    font-weight: 600;
    letter-spacing: 0.5px;
    line-height: 1;
  }

  /* Back */
  .card-back { top: 513px; background: var(--card-light); border: 1px solid #d6d6d6; }
  .appt-title {
    position: absolute; top: 19px; left: 0; width: 100%;
    text-align: center; font-size: 18px; text-decoration: underline;
    text-underline-offset: 3px; color: var(--ink);
  }
  .field-label { position: absolute; font-size: 17px; color: var(--ink); }
  .col-head {
    position: absolute; font-size: 16px; color: var(--ink);
    text-decoration: underline; text-underline-offset: 3px;
  }
  .dotted-line {
    position: absolute; height: 0;
    border-bottom: 1px dashed var(--ink-soft);
  }
  .divider-v {
    position: absolute; left: 309px; top: 160px;
    width: 1px; height: 100px; background: var(--rule);
  }
  .divider-h {
    position: absolute; left: 60px; top: 300px;
    width: 502px; height: 1px; background: var(--rule);
  }
  .contact {
    position: absolute; top: 318px; left: 0; width: 100%;
    display: flex; justify-content: center; align-items: center;
    font-size: 16px; color: var(--ink);
  }
  .contact svg { display: block; }
  .contact .address { margin-left: 3px; }
  .contact .phone-icon { margin-left: 10px; }
  .contact .phone { margin-left: 4px; }
</style>
</head>
<body>
<main class="canvas">
  <section class="card card-front">
    <div class="brand">
      <div class="brand-name">Marisol Denby</div>
      <div class="brand-tagline">HAIR SALON</div>
    </div>
  </section>

  <section class="card card-back">
    <div class="appt-title">Appointments</div>

    <div class="field-label" style="left:46px; top:73px;">Name:</div>
    <div class="dotted-line" style="left:117px; width:456px; top:92px;"></div>

    <div class="col-head" style="left:46px; top:127px;">Date</div>
    <div class="col-head" style="left:236px; top:127px;">Time</div>
    <div class="col-head" style="left:346px; top:127px;">Date</div>
    <div class="col-head" style="left:535px; top:127px;">Time</div>

    <div class="dotted-line" style="left:46px; width:228px; top:181px;"></div>
    <div class="dotted-line" style="left:46px; width:228px; top:216px;"></div>
    <div class="dotted-line" style="left:46px; width:228px; top:251px;"></div>
    <div class="dotted-line" style="left:346px; width:228px; top:181px;"></div>
    <div class="dotted-line" style="left:346px; width:228px; top:216px;"></div>
    <div class="dotted-line" style="left:346px; width:228px; top:251px;"></div>

    <div class="divider-v"></div>
    <div class="divider-h"></div>

    <div class="contact">
      <svg width="16" height="22" viewBox="0 0 16 22" aria-hidden="true">
        <path d="M8 0C3.6 0 0 3.5 0 7.9 0 13.6 8 22 8 22s8-8.4 8-14.1C16 3.5 12.4 0 8 0z" fill="#555"/>
        <circle cx="8" cy="7.9" r="3" fill="#fff"/>
      </svg>
      <span class="address">362 Thistledown Lane York, PA 17488</span>
      <svg class="phone-icon" width="22" height="22" viewBox="0 0 22 22" aria-hidden="true">
        <circle cx="11" cy="11" r="10" fill="none" stroke="#555" stroke-width="1.3"/>
        <path d="M8 5.5c.6-.4 1.3-.2 1.6.4l.9 1.8c.3.6.1 1.2-.4 1.5l-.8.5c.3 1.6 1.2 3.2 2.5 4.3l.8-.4c.6-.3 1.2-.1 1.5.5l.9 1.7c.3.6.1 1.3-.5 1.6l-.9.5c-3.6-1.2-6.3-5.4-6.3-9.6z" fill="#555"/>
      </svg>
      <span class="phone">717 555 0148</span>
    </div>
  </section>
</main>
</body>
</html>
```